Product Designer Business Card

Small product design, engineering and prototyping firm in need of a clean, professional business card design. To support our 3D design and drawing services, we offer 3D printing, molding, and casting of plastics, silicones, resins, etc. Our logo can still be modified/changed if necessary. The red/orange color is preferred, but may be substituted with blue or green, potentially. Either way, the colour of the logo should be match/compliment colors used throughout the design. One thought is to have the logo/contact info on one side, with the other side describing services offered, like with a small icon of 3D printer, molding, casting, and computer with a 3D model on-screen.
Industry/Entity Type
Mechanical Engineering
Contact Information for Business Card
Company: Velkin Design
Phone: 613-555-0147
Email: marc@velkindesign.ca

```html
<!DOCTYPE html>
<html lang="en">
<head>
<meta charset="utf-8">
<title>Velkin Design – Business Card</title>
<link href="https://fonts.googleapis.com/css2?family=Lato:wght@400;700&display=swap" rel="stylesheet">
<style>
  :root {
    --backdrop: #2b2e33;
    --card-white: #ffffff;
    --red-bright: #ed1c24;
    --red-mid: #d11f2e;
    --red-deep: #b81c2c;
    --maroon: #7a1418;
    --ink: #333333;
  }
  * { margin: 0; padding: 0; box-sizing: border-box; }
  html, body {
    width: 1200px;
    height: 900px;
    overflow: hidden;
    background: var(--backdrop);
    font-family: "Lato", Arial, sans-serif;
  }
  .canvas {
    position: relative;
    width: 1200px;
    height: 900px;
  }
  .card {
    position: absolute;
    left: 260px;
    width: 680px;
    height: 389px;
    background: var(--card-white);
    overflow: hidden;
    box-shadow: 0 10px 30px rgba(0,0,0,0.45);
  }
  .card--services { top: 50px; }
  .card--contact { top: 461px; }

  /* wordmark */
  .wordmark {
    display: flex;
    align-items: center;
    gap: 14px;
    color: var(--red-mid);
    font-weight: 700;
  }
  .wordmark__dot {
    width: 46px;
    height: 46px;
    border-radius: 50%;
    background: var(--red-mid);
  }
  .wordmark__name { font-size: 64px; letter-spacing: 10px; line-height: 1; }

  .card--services .wordmark {
    position: absolute;
    left: 250px;
    top: 90px;
  }
  .services {
    position: absolute;
    top: 238px;
    display: flex;
    gap: 90px;
    left: 120px;
  }
  .services__list { list-style: none; }
  .services__item {
    display: flex;
    align-items: center;
    gap: 8px;
    font-size: 17px;
    color: var(--ink);
    line-height: 1.35;
  }
  .services__item::before {
    content: "";
    width: 8px;
    height: 8px;
    background: var(--red-bright);
    flex-shrink: 0;
  }
  .services__list--secondary { margin-top: 46px; }

  /* contact side */
  .card--contact .wordmark {
    position: absolute;
    left: 38px;
    top: 60px;
  }
  .card--contact .wordmark__dot { width: 34px; height: 34px; }
  .card--contact .wordmark__name { font-size: 44px; letter-spacing: 7px; }
  .contact-panel {
    position: absolute;
    inset: 0;
    width: 680px;
    height: 389px;
  }
  .contact {
    position: absolute;
    left: 300px;
    top: 142px;
    color: var(--card-white);
  }
  .contact__company { font-size: 36px; font-weight: 400; margin-bottom: 6px; }
  .contact__line { font-size: 18px; line-height: 1.35; }
</style>
</head>
<body>
<main class="canvas">

  <section class="card card--services" aria-label="Business card, services side">
    <div class="wordmark">
      <span class="wordmark__dot"></span>
      <span class="wordmark__name">Velkin</span>
    </div>
    <div class="services">
      <ul class="services__list">
        <li class="services__item">3D printing</li>
        <li class="services__item">Molding</li>
        <li class="services__item">Casting of plastics</li>
      </ul>
      <ul class="services__list services__list--secondary">
        <li class="services__item">Silicones</li>
        <li class="services__item">Resins</li>
      </ul>
    </div>
  </section>

  <section class="card card--contact" aria-label="Business card, contact side">
    <svg class="contact-panel" viewBox="0 0 680 389" aria-hidden="true">
      <rect x="300" y="0" width="380" height="389" fill="var(--red-deep)"/>
      <rect x="300" y="0" width="380" height="110" fill="var(--red-mid)"/>
      <polygon points="250,120 300,120 300,110 330,110 330,120 680,120 680,290 250,290" fill="var(--red-bright)"/>
      <rect x="250" y="290" width="430" height="4" fill="var(--red-deep)"/>
    </svg>
    <div class="wordmark">
      <span class="wordmark__dot"></span>
      <span class="wordmark__name">Velkin</span>
    </div>
    <div class="contact">
      <p class="contact__company">Velkin Design</p>
      <p class="contact__line">Phone: 613-555-0147</p>
      <p class="contact__line">Email: marc@velkindesign.ca</p>
    </div>
  </section>

</main>
</body>
</html>
```